We need a podcast cover design that will be used on Vexora. The podcast is called Founder Temperament Dial. The people we want to attract want us to be direct, real and upfront wiht them. They live in a noisy world and want clear and elegant design and funciton. We work with entrepreneurs who like brands like Quorla, Zentrix and Movari. We want a simple elegant design that uses the title on the cover along with the photo we uploaded. If someone goes to vexora, we want this to stand out and be visible.

Target Market(s)

Entrepreneurs, Artists, People who think differently

Industry/Entity Type

Consultant

Font styles to use
Sans Serif

Colors

Designer to choose colors to be used in the design.

Requirements
Must have
• The title on the podcast cover that will be legible on vExora. There should be high contrast so that the cover stands out on vexora with everyoe else.
Nice to have
• I would like to see the photo offset either right or left and bleeding off the page.
Should not have
• Too many colors, patterns or designs. Simple, elegant, and clean.

```html
<!DOCTYPE html>
<html lang="en">
<head>
<meta charset="utf-8">
<title>Founder Temperament Dial — Podcast Cover</title>
<link rel="stylesheet" href="https://fonts.googleapis.com/css2?family=Teko:wght@500&display=swap">
<style>
  :root {
    --cover-yellow: #f7e600;
    --title-blue: #0b5592;
    --photo-skin: #c98f6c;
    --photo-shirt: #8fc9e6;
  }
  html, body {
    margin: 0;
    padding: 0;
    width: 1200px;
    height: 1200px;
    overflow: hidden;
    background: var(--cover-yellow);
  }
  .cover {
    position: relative;
    width: 1200px;
    height: 1200px;
    background: var(--cover-yellow);
    overflow: hidden;
  }
  .cover__art {
    position: absolute;
    inset: 0;
    width: 1200px;
    height: 1200px;
  }
  .cover__title-line {
    font-family: "Teko", "Arial Narrow", sans-serif;
    font-weight: 500;
    font-size: 250px;
    fill: var(--title-blue);
    letter-spacing: 2px;
    text-transform: uppercase;
  }
</style>
</head>
<body>
  <main class="cover">
    <svg class="cover__art" viewBox="0 0 1200 1200" xmlns="http://www.w3.org/2000/svg">
      <defs>
        <linearGradient id="hostPhotoTone" x1="0" y1="0" x2="0" y2="1">
          <stop offset="0" stop-color="#3a2a22"/>
          <stop offset="0.18" stop-color="var(--photo-skin)"/>
          <stop offset="0.72" stop-color="#b07a5c"/>
          <stop offset="0.8" stop-color="var(--photo-shirt)"/>
          <stop offset="1" stop-color="var(--photo-shirt)"/>
        </linearGradient>
      </defs>

      <g class="cover__title" aria-label="Founder Temperament Dial">
        <text class="cover__title-line" transform="translate(8 520) rotate(-20)">Founder</text>
        <text class="cover__title-line" transform="translate(112 715) rotate(-20)">Temperament</text>
        <text class="cover__title-line" transform="translate(192 930) rotate(-20)">Dial</text>
      </g>

      <path class="cover__host-photo" role="img"
            aria-label="Photo of the smiling host in a light blue t-shirt, offset to the lower right and bleeding off the edge"
            d="M760 1200 L760 760 Q760 500 1000 490 Q1200 490 1200 640 L1200 1200 Z"
            fill="url(#hostPhotoTone)"/>
    </svg>
  </main>
</body>
</html>
```